Flyer-Design für Ferienhausvermietung
Zielgruppe
Wir haben ein Ferienhaus zu vermieten.
Hauptzielgruppe sind hierbei:
Wanderer/Radfahrer
ältere Personen
gebildet
gerne mit Hund
Aufgabenstellung
Es soll ein Flyer im Format DIN A4 erstellt werden.
Der beidseitig bedruckt wird und dann 6seitig gefaltet wird.
Ich benötige für den Flyer:
Beschreibung/Ausstattung des Ferienhauses
Beschreibung der Lage
Beschreibung der Umgebung
Anfahrt/Lage/Kontakt

```html
<!DOCTYPE html>
<html lang="de">
<head>
<meta charset="utf-8">
<title>Ferienhaus zu vermieten – Faltflyer</title>
<link rel="stylesheet" href="https://fonts.googleapis.com/css2?family=Comfortaa:wght@400;700&family=Quicksand:wght@400;500;600;700&display=swap">
<style>
:root{
  --green:#8cbf26;
  --green-dark:#6f9d17;
  --slate:#33434f;
  --paper:#f4f4f4;
  --white:#ffffff;
  --ink:#2c3338;
  --stage:#e4e7e9;
}
*{box-sizing:border-box;margin:0;padding:0}
html,body{width:1200px;height:1200px;overflow:hidden;background:var(--stage)}
body{font-family:"Quicksand",sans-serif;color:var(--ink);position:relative}
.spread{position:absolute;left:200px;width:800px;height:566px;background:var(--paper);overflow:hidden;box-shadow:0 6px 18px rgba(0,0,0,.12)}
.spread--outside{top:14px}
.spread--inside{top:620px}
.spread-shapes{position:absolute;inset:0;width:800px;height:566px}
.abs{position:absolute}
.photo{position:absolute;border:4px solid var(--green);border-radius:16px;overflow:hidden}
.heading{font-family:"Comfortaa",sans-serif;color:var(--green);font-size:15px;font-weight:700;border-bottom:1.5px solid var(--green);padding-bottom:3px}
/* outside: back flap */
.region{left:20px;top:18px;width:235px;text-align:right;font-family:"Comfortaa",sans-serif}
.region-name{color:var(--green);font-size:13px;line-height:1.35}
.region-tags{color:var(--white);font-size:13px;margin-top:2px}
/* outside: contact panel */
.contact-title{left:285px;top:416px;font-family:"Comfortaa",sans-serif;font-weight:700;color:var(--white);font-size:17px;letter-spacing:1px}
.contact-list{left:285px;top:446px;width:240px;list-style:none;color:var(--white);font-size:10.5px;line-height:1.55}
.contact-list li{display:flex;gap:7px;align-items:flex-start}
.contact-list svg{flex:none;margin-top:2px}
/* outside: cover */
.cover-title{left:560px;top:120px;width:225px;text-align:right;color:var(--white);font-family:"Comfortaa",sans-serif;font-weight:700;font-size:31px;line-height:1.12;text-shadow:0 1px 4px rgba(0,0,0,.35)}
.audience{left:560px;top:284px;width:225px;text-align:right;color:var(--green);font-family:"Comfortaa",sans-serif;font-weight:700;font-size:12.5px;line-height:1.45}
.intro{left:548px;top:340px;width:236px;font-size:10px;line-height:1.42;color:var(--ink);font-weight:500}
/* inside */
.facts-title{left:285px;top:18px;font-family:"Comfortaa",sans-serif;font-weight:700;color:var(--white);font-size:15px}
.facts-list{left:285px;top:40px;width:360px;list-style:none;color:var(--white);font-size:10px;line-height:1.45;font-weight:600}
.prices-title{left:285px;top:170px;font-family:"Comfortaa",sans-serif;font-weight:700;color:var(--green);font-size:15px}
.price-table{left:285px;top:192px;width:300px;border-collapse:collapse;font-size:10px;font-weight:600}
.price-table td{padding:1px 0;vertical-align:top}
.price-table .amount{color:var(--slate);font-weight:700;text-align:right;padding-right:4px;white-space:nowrap}
.price-table .unit{font-size:8.5px;white-space:nowrap}
.price-notes{left:285px;top:268px;width:260px;font-size:10px;line-height:1.45;font-weight:600}
.price-date{left:285px;top:304px;color:var(--green);font-size:10px;font-weight:600}
</style>
</head>
<body>

<section class="spread spread--outside" aria-label="Flyer Außenseite">
  <svg class="spread-shapes" viewBox="0 0 800 566" aria-hidden="true">
    <rect width="800" height="566" fill="var(--paper)"/>
    <path d="M0 0 H267 V78 Q150 128 0 118 Z" fill="var(--slate)"/>
    <path d="M0 360 Q40 520 267 548 V566 H0 Z" fill="var(--slate)"/>
    <path d="M0 330 Q30 500 240 566 H0 Z" fill="var(--green)"/>
    <rect x="267" y="0" width="266" height="566" fill="var(--green)"/>
    <path d="M267 535 Q300 556 390 566 H267 Z" fill="var(--slate)"/>
    <path d="M533 250 Q650 320 800 262 V566 H533 Z" fill="var(--white)"/>
    <path d="M450 0 H800 V268 Q650 335 520 240 Q458 170 450 0 Z" fill="var(--white)"/>
    <path d="M533 505 Q700 505 800 478 V566 H533 Z" fill="var(--slate)"/>
    <path d="M640 566 Q740 545 800 515 V566 Z" fill="var(--green)"/>
  </svg>

  <div class="abs" role="img" aria-label="Luftbild: Ferienhaus im herbstlichen Tal mit Wiesen und Wald, Standortmarkierung"
       style="left:456px;top:0;width:344px;height:262px;background:linear-gradient(160deg,#c7a24b 0%,#7fa33a 40%,#5f8a2c 70%,#b8702f 100%);clip-path:path('M0 0 H344 V262 Q196 330 66 238 Q4 170 0 0 Z')"></div>

  <p class="region abs">
    <span class="region-name">Rhön/Thüringer<br>Wald/Meiningen</span><br>
    <span class="region-tags">Kultur, Wandern, Radfahren..</span>
  </p>
  <h3 class="heading abs" style="left:22px;top:128px;width:140px">Badezimmer</h3>
  <div class="photo" role="img" aria-label="Foto: Badezimmer mit Waschtisch, Spiegel und Holztür"
       style="left:36px;top:160px;width:210px;height:150px;background:linear-gradient(135deg,#e7e3dc,#b7a48d 60%,#6f5a45)"></div>
  <div class="photo" role="img" aria-label="Foto: Duschkabine und WC mit Holzboden"
       style="left:24px;top:316px;width:210px;height:160px;background:linear-gradient(135deg,#d9d6d1,#c3b19b 55%,#6e5a47)"></div>

  <div class="abs" role="img" aria-label="Illustration: zwei Radfahrer"
       style="left:300px;top:270px;width:200px;height:70px;background:linear-gradient(90deg,#a9d35a,#c6e68a);border-radius:10px;opacity:.8"></div>
  <div class="abs" role="img" aria-label="Lageplan des Ferienhauses"
       style="left:285px;top:350px;width:230px;height:56px;background:#eef0f2;border-radius:14px;border:3px solid var(--white)"></div>

  <h3 class="contact-title abs">KONTAKTDATEN:</h3>
  <ul class="contact-list abs">
    <li><svg width="9" height="12" viewBox="0 0 9 12"><path d="M4.5 0A4.5 4.5 0 0 0 0 4.5C0 8 4.5 12 4.5 12S9 8 9 4.5A4.5 4.5 0 0 0 4.5 0Z" fill="var(--slate)"/><circle cx="4.5" cy="4.5" r="1.7" fill="var(--green)"/></svg>
      <span>Marlene Vogt und Tobias Quast<br>Am Mühlgrund 3, 98999 Talheim/OT Unterau<br>0170/4417823</span></li>
    <li><svg width="11" height="8" viewBox="0 0 11 8"><rect width="11" height="8" rx="1" fill="var(--slate)"/><path d="M0.5 0.8 5.5 4.6 10.5 0.8" stroke="var(--green)" stroke-width="1" fill="none"/></svg>
      <span>toblerquast69@postfach-mail.de</span></li>
  </ul>

  <h1 class="cover-title abs">Ferienhaus<br>zu vermieten.</h1>
  <p class="audience abs">Wanderer/Naturliebhaber,<br>ab 30 Jahre,<br>gebildet, gerne mit Hund.</p>
  <p class="intro abs">Ehemaliger Bauern- und Mühlenhof aufwendig saniert und restauriert mit viel Liebe zum Detail mitten auf der Bayerisch-Thüringischen Grenze. Über das Grundstück verläuft ein kleiner Bach. Ein schönes Fleckchen Erde in ruhiger Lage am Waldrand und dennoch mit sehr günstigen Verkehrsanbindung. In nur 10 Minuten zur nächst größeren Stadt bzw. zu A71.</p>
  <div class="abs" role="img" aria-label="Illustration: Wanderer mit Hund"
       style="left:690px;top:500px;width:95px;height:58px;background:linear-gradient(90deg,#eef3e4,#ffffff);border-radius:8px;opacity:.85"></div>
</section>

<section class="spread spread--inside" aria-label="Flyer Innenseite">
  <svg class="spread-shapes" viewBox="0 0 800 566" aria-hidden="true">
    <rect width="800" height="566" fill="var(--paper)"/>
    <path d="M0 0 H230 Q70 40 20 230 L0 250 Z" fill="var(--slate)"/>
    <path d="M267 0 Q120 20 70 150 Q40 260 0 300 V250 Q40 120 150 30 Q200 0 267 0 Z" fill="var(--green)"/>
    <path d="M0 500 Q120 560 267 540 V566 H0 Z" fill="var(--green)"/>
    <path d="M267 0 H800 V40 Q660 150 267 150 Z" fill="var(--green)"/>
  </svg>

  <div class="abs" role="img" aria-label="Luftbild: Hofanlage mit roten Dächern, markiertes Ferienhaus"
       style="left:267px;top:330px;width:533px;height:236px;background:linear-gradient(160deg,#9bbf4a,#6d9a30 45%,#a5532f 75%,#6f8d35);clip-path:path('M0 80 Q250 0 533 40 V236 H0 Z')"></div>

  <div class="abs" role="img" aria-label="Illustration: zwei Wanderer"
       style="left:95px;top:80px;width:100px;height:66px;background:linear-gradient(90deg,#b5d975,#8cbf26);border-radius:8px;opacity:.8"></div>
  <h3 class="heading abs" style="left:60px;top:155px;width:200px;text-align:center">Wohnzimmer/Küche</h3>
  <div class="photo" role="img" aria-label="Foto: Wohnzimmer mit Holzbalken, Tür und Essplatz"
       style="left:30px;top:186px;width:228px;height:168px;background:linear-gradient(135deg,#ddd7cc,#8d6a4a 55%,#4e3a2a)"></div>
  <div class="photo" role="img" aria-label="Foto: Küche und Sitzecke mit Holzboden"
       style="left:20px;top:360px;width:238px;height:170px;background:linear-gradient(135deg,#e2ddd4,#3f5248 35%,#8c6a4c 70%,#4d3a2b)"></div>

  <h3 class="facts-title abs">ECKDATEN:</h3>
  <ul class="facts-list abs">
    <li>Nichtraucherwohnung bestehend aus Wohnzimmer/Küche, Badezimmer,</li>
    <li>1 Schlafzimmer</li>
    <li>für bis zu 4 Personen</li>
    <li>Terrasse und Parkplatz direkt am Ferienhaus</li>
    <li>Hunde willkommen</li>
  </ul>

  <h3 class="prices-title abs">PREISE:</h3>
  <table class="price-table abs">
    <tr><td>für 2 Pers.</td><td class="amount">86€</td><td class="unit">pro Übernachtung</td></tr>
    <tr><td>ab 4 Übernachtungen zzgl.</td><td class="amount">76€</td><td class="unit">pro Übernachtung</td></tr>
    <tr><td>für die 3 und 4 Person</td><td class="amount">22€</td><td class="unit">je Person und Übernachtung</td></tr>
    <tr><td>Pro Hund und Übernachtung</td><td class="amount">5€</td><td class="unit">pro Hund und Übernachtung</td></tr>
  </table>
  <p class="price-notes abs">Mindestaufenthalt 2 Übernachtungen<br>Preise verstehen sich inkl. aller Nebenkosten</p>
  <p class="price-date abs">(Stand Okt. 2020)</p>

  <h3 class="heading abs" style="left:640px;top:136px;width:150px;text-align:right">Schlafzimmer</h3>
  <div class="photo" role="img" aria-label="Foto: Schlafzimmer mit Tagesbett und kariertem Bettzeug"
       style="left:580px;top:164px;width:205px;height:150px;background:linear-gradient(135deg,#f0ede8,#c9b9a4 50%,#b33a33 75%,#7a5d44)"></div>
  <div class="photo" role="img" aria-label="Foto: Dachgeschoss mit Treppe und Schlafplatz"
       style="left:590px;top:320px;width:200px;height:160px;background:linear-gradient(135deg,#ebe8e2,#a58a6d 55%,#5a4433)"></div>
</section>

</body>
</html>
```